Business Cards, Letterheads, Envelopes

A company's new identity to be reflected on its stationery items

Target Market(s)

Large Corporate Companies & Enterprises

Font styles to use
Sans Serif

Colors
0555a3
3176b5
85abd2
85cae6
33a6d7
0293ce

```html
<!DOCTYPE html>
<html lang="en">
<head>
<meta charset="utf-8">
<title>Veralink Systems — Stationery</title>
<link href="https://fonts.googleapis.com/css2?family=Lato:wght@300;400;700&family=Roboto:wght@400;500&display=swap" rel="stylesheet">
<style>
:root{
  --blue:#3176b5;
  --blue-mid:#5287c2;
  --blue-soft:#85abd2;
  --blue-deep:#0555a3;
  --paper:#ffffff;
  --env:#f4f5f6;
  --ink:#3a3a3a;
  --ink-soft:#6b6b6b;
  --grey-band:#9a9a9a;
  --bg:#dcdddf;
}
*{box-sizing:border-box;margin:0;padding:0}
html,body{width:1200px;height:960px;overflow:hidden}
body{background:var(--bg);font-family:'Lato',sans-serif;color:var(--ink);position:relative}
.sheet{position:absolute;background:var(--paper);box-shadow:0 6px 18px rgba(0,0,0,.12)}
.brand{color:var(--blue);font-family:'Lato',sans-serif;font-weight:700;text-transform:uppercase;letter-spacing:.08em;display:flex;align-items:center;gap:8px}
.brand-dot{display:inline-block;border-radius:50%;background:var(--blue)}

/* letterhead */
.letterhead{left:40px;top:40px;width:540px;height:764px;padding:44px 50px}
.letterhead .brand{font-size:15px}
.letterhead .brand-dot{width:22px;height:22px}
.letterhead .decor{position:absolute;right:0;top:150px;width:160px;height:180px;background:linear-gradient(135deg,var(--blue-soft),var(--blue));opacity:.85}
.letter{position:absolute;left:50px;top:150px;width:330px;font-size:9.5px;line-height:1.5;font-weight:300}
.letter .date{margin-bottom:12px}
.letter .recipient{margin-bottom:14px}
.letter .recipient strong{font-weight:700}
.letter p{text-align:justify;margin-bottom:10px}
.letter .sign{margin-top:22px}
.letter-foot{position:absolute;left:50px;bottom:60px;right:50px;display:flex;align-items:center;gap:16px;font-family:'Roboto',sans-serif;font-size:10px;line-height:1.45}
.divider{width:1px;height:30px;background:var(--ink)}
.contact-line{display:flex;align-items:center;gap:6px}
.contact-line svg{width:9px;height:9px;flex:none}
.web{position:absolute;right:50px;bottom:28px;font-family:'Roboto',sans-serif;font-size:11px}
.web span{color:var(--blue)}

/* cards */
.card{width:300px;height:171px;overflow:hidden}
.card-front{left:620px;top:60px}
.card-front .brand{position:absolute;left:18px;top:14px;font-size:10px}
.card-front .brand-dot{width:12px;height:12px}
.card-front .band{position:absolute;left:0;top:46px;width:300px;height:62px;background:var(--blue-mid)}
.card-front .band-grey{position:absolute;right:0;top:46px;width:40px;height:62px;background:var(--grey-band)}
.card-front .band-circle{position:absolute;right:26px;top:52px;width:50px;height:50px;border-radius:50%;background:var(--paper)}
.card-front .person{position:absolute;left:18px;top:52px;color:#fff;font-size:7px;line-height:1.35}
.card-front .person .name{font-size:10px;font-weight:700}
.card-front .person .role{margin-bottom:3px}
.card-front .person .contact-line svg{width:6px;height:6px}
.card-front .company{position:absolute;left:18px;top:120px;font-size:7px;line-height:1.4}
.card-front .company strong{color:var(--blue);font-weight:700}

.card-back{left:620px;top:270px;background:var(--blue-mid)}
.card-back .decor{position:absolute;left:0;top:0;width:130px;height:171px;background:linear-gradient(160deg,var(--blue-soft),var(--blue-mid))}
.card-back .site{position:absolute;right:18px;top:24px;color:#fff;font-size:7px}
.card-back .site b{font-weight:700}
.card-back .brand{position:absolute;right:18px;bottom:30px;color:#fff;font-size:11px}

/* envelope */
.envelope{left:620px;top:500px;width:540px;height:270px;background:var(--env)}
.envelope .brand{position:absolute;left:30px;top:26px;font-size:13px}
.envelope .brand-dot{width:18px;height:18px}
.envelope .return{position:absolute;left:30px;top:176px;display:flex;align-items:center;gap:14px;font-family:'Roboto',sans-serif;font-size:9.5px;line-height:1.45}
.envelope .return .co{color:var(--blue)}
.envelope .web{right:30px;bottom:22px;font-size:10px}
</style>
</head>
<body>

<!-- Letterhead -->
<section class="sheet letterhead">
  <div class="brand"><span class="brand-dot"></span>Veralink Systems Private Limited</div>
  <div class="decor" role="img" aria-label="Decorative blue graphic area"></div>
  <div class="letter">
    <div class="date">01 January 2050</div>
    <div class="recipient"><strong>Company (Pvt) Ltd.</strong><br>PO Box 3355 Mainville St<br>Sample City Country 3355</div>
    <p>Dear Daniel Reyes,</p>
    <p>Lorem ipsum dolor sit amet, consectetuer adipiscing elit, sed diam nonummy nibh euismod tincidunt ut laoreet dolore magna aliquam erat volutpat. Ut wisi enim ad minim veniam, quis nostrud exerci tation ullamcorper suscipit lobortis nisl ut aliquip ex ea commodo consequat. Duis dolore te feugait nulla facilisi. Nam liber tempor cum soluta nobis eleifend option congue nihil imperdiet doming id quod mazim placerat facer possim assum. Lorem ipsum dolor sit amet, consectetuer adipiscing elit, sed diam nonummy nibh euismod tincidunt ut laoreet dolore magna aliquam erat volutpat. Ut wisi enim ad minim veniam, quis nostrud exerci tation ullamcorper suscipit lobortis nisl ut aliquip ex ea commodo consequat.</p>
    <p>Consectetuer adipiscing elit, sed diam nonummy nibh euismod tincidunt ut laoreet dolore magna aliquam erat volutpat. Ut wisi enim ad minim veniam, quis nostrud exerci tation ullamcorper suscipit lobortis nisl ut aliquip ex ea commodo consequat. Consectetuer adipiscing elit, sed diam nonummy nibh euismod tincidunt ut laoreet dolore magna aliquam erat volutpat.</p>
    <p>Consectetuer adipiscing elit, sed diam nonummy nibh euismod tincidunt ut laoreet dolore magna aliquam erat volutpat. Ut wisi enim ad minim veniam, quis nostrud exerci tation ullamcorper suscipit lobortis nisl ut aliquip ex ea commodo consequat.</p>
    <div class="sign">Sincerely Yours</div>
  </div>
  <div class="letter-foot">
    <div>14B, Lakeview Tech Park<br>Kengeri, Bengaluru, Karnataka</div>
    <div class="divider"></div>
    <div>
      <div class="contact-line"><svg viewBox="0 0 10 10"><path d="M2 1l2 2-1 1.2c.6 1.2 1.6 2.2 2.8 2.8L7 6l2 2-1.2 1.2C4.5 9 1 5.5.8 2.2z" fill="var(--blue)"/></svg>+91 800 555 0192</div>
      <div class="contact-line"><svg viewBox="0 0 10 10"><rect x=".8" y="2" width="8.4" height="6" fill="none" stroke="var(--blue)"/><path d="M.8 2L5 5.5 9.2 2" fill="none" stroke="var(--blue)"/></svg>hello@veralinksys.com</div>
    </div>
  </div>
  <div class="web">www.<span>veralinksys</span>.com</div>
</section>

<!-- Business card front -->
<section class="sheet card card-front">
  <div class="brand"><span class="brand-dot"></span>Veralink Systems</div>
  <div class="band"></div>
  <div class="band-grey"></div>
  <div class="band-circle"></div>
  <div class="person">
    <div class="name">Arun Mehra</div>
    <div class="role">CEO &amp; Founder</div>
    <div class="contact-line"><svg viewBox="0 0 10 10"><path d="M2 1l2 2-1 1.2c.6 1.2 1.6 2.2 2.8 2.8L7 6l2 2-1.2 1.2C4.5 9 1 5.5.8 2.2z" fill="#fff"/></svg>+91 800 555 0192</div>
    <div class="contact-line"><svg viewBox="0 0 10 10"><rect x=".8" y="2" width="8.4" height="6" fill="none" stroke="#fff"/><path d="M.8 2L5 5.5 9.2 2" fill="none" stroke="#fff"/></svg>hello@veralinksys.com</div>
    <div class="contact-line"><svg viewBox="0 0 10 10"><circle cx="5" cy="5" r="4" fill="none" stroke="#fff"/><path d="M1 5h8M5 1c-2 2.5-2 5.5 0 8M5 1c2 2.5 2 5.5 0 8" fill="none" stroke="#fff" stroke-width=".7"/></svg>www.veralinksys.com</div>
  </div>
  <div class="company"><strong>Veralink Systems (Pvt) Ltd.</strong><br>14B, Lakeview Tech Park, Kengeri, Bengaluru, Karnataka</div>
</section>

<!-- Business card back -->
<section class="sheet card card-back">
  <div class="decor" role="img" aria-label="Decorative blue graphic area"></div>
  <div class="site">www.<b>veralinksys</b>.com</div>
  <div class="brand">Veralink Systems</div>
</section>

<!-- Envelope -->
<section class="sheet envelope">
  <div class="brand"><span class="brand-dot"></span>Veralink Systems Private Limited</div>
  <div class="return">
    <div><span class="co">Veralink Systems (Pvt) Ltd.</span><br>14B, Lakeview Tech Park<br>Kengeri, Bengaluru, Karnataka</div>
    <div class="divider"></div>
    <div>
      <div class="contact-line"><svg viewBox="0 0 10 10"><path d="M2 1l2 2-1 1.2c.6 1.2 1.6 2.2 2.8 2.8L7 6l2 2-1.2 1.2C4.5 9 1 5.5.8 2.2z" fill="var(--blue)"/></svg>+91 800 555 0192</div>
      <div class="contact-line"><svg viewBox="0 0 10 10"><rect x=".8" y="2" width="8.4" height="6" fill="none" stroke="var(--blue)"/><path d="M.8 2L5 5.5 9.2 2" fill="none" stroke="var(--blue)"/></svg>hello@veralinksys.com</div>
    </div>
  </div>
  <div class="web">www.<span>veralinksys</span>.com</div>
</section>

</body>
</html>
```